Business Card Design

I need a business card for my rental business. The business is named:
Hire a Vorlatrike Brenmoor
www.hireavorlatrikebrenmoor.example
(555) 014-2937
This will be a business card that I will leave at other businesses as advertisement so it needs to have the name, website, and phone number.
Please feel free to be creative. This is a new business so I have no designs.
Thank you very much for your time and I look forward to receiving your designs
Target Market(s)
Local rental customers
Industry/Entity Type
Business
Contact Information for Business Card
Please check out my website:
Other font styles liked:
- anything creative
Colors
Designer to choose colors to be used in the design.
Requirements
Must have
- Business name, phone, website. Rentals available hourly or daily. Book online

```html
<!DOCTYPE html>
<html lang="en">
<head>
<meta charset="utf-8">
<title>Hire a Vorlatrike Brenmoor – Business Cards</title>
<link rel="stylesheet" href="https://fonts.googleapis.com/css2?family=Arimo:wght@400;700&display=swap">
<style>
  :root {
    --page-bg: #ffffff;
    --panel-grey: #e0e0df;
    --light-end: #dcdcdb;
    --mono-dark: #1f1b19;
    --mono-text: #1f1b19;
    --blue-dark: #0f5585;
    --blue-light: #d9e0e5;
    --blue-text: #1b4a86;
    --white: #ffffff;
  }
  * { box-sizing: border-box; margin: 0; padding: 0; }
  html, body {
    width: 1200px; height: 848px; overflow: hidden;
    background: var(--page-bg);
    font-family: "Arimo", Arial, sans-serif;
  }
  .canvas { position: relative; width: 1200px; height: 848px; }

  .card {
    position: absolute; left: 345px; width: 510px; height: 321px;
    display: flex; flex-direction: column;
  }
  .card--mono { top: 72px; --accent: var(--mono-dark); --ink: var(--mono-text); --fade: var(--light-end); }
  .card--blue { top: 452px; --accent: var(--blue-dark); --ink: var(--blue-text); --fade: var(--blue-light); }

  .hero {
    position: relative; height: 157px;
    background: linear-gradient(90deg, var(--fade) 0%, var(--fade) 12%, var(--accent) 100%);
    color: var(--white);
  }
  .hero__vehicle {
    position: absolute; left: 8px; top: 11px; width: 200px; height: 126px;
    background: radial-gradient(ellipse at 50% 55%, rgba(0,0,0,0.12), rgba(0,0,0,0) 70%);
  }
  .card--blue .hero__vehicle {
    background: radial-gradient(ellipse at 50% 55%, rgba(15,85,133,0.18), rgba(15,85,133,0) 70%);
  }
  .hero__title {
    position: absolute; left: 240px; top: 14px;
    font-size: 64px; font-weight: 700; line-height: 1;
  }
  .hero__subtitle {
    position: absolute; right: 40px; top: 99px;
    font-size: 23px; font-weight: 400; line-height: 1;
  }

  .contact {
    position: relative; height: 115px; background: var(--panel-grey); color: var(--ink);
  }
  .contact__phone {
    position: absolute; right: 15px; top: 25px;
    display: flex; align-items: center; gap: 10px;
    font-size: 19px; font-weight: 700; letter-spacing: 0.5px;
  }
  .contact__web {
    position: absolute; right: 15px; top: 62px;
    display: flex; align-items: center; gap: 8px;
    font-size: 22px; font-weight: 700;
  }
  .icon { display: block; fill: none; stroke: currentColor; }

  .tagline {
    height: 49px; background: var(--accent); color: var(--white);
    display: flex; align-items: center; justify-content: center;
    font-size: 19px; font-weight: 400;
  }
</style>
</head>
<body>
<main class="canvas">

  <section class="card card--mono">
    <div class="hero">
      <div class="hero__vehicle" role="img" aria-label="Line illustration of a three-wheeled roadster"></div>
      <div class="hero__title">Hire</div>
      <div class="hero__subtitle">a Vorlatrike Brenmoor</div>
    </div>
    <div class="contact">
      <div class="contact__phone">
        <svg class="icon" width="16" height="32" viewBox="0 0 16 32" aria-hidden="true">
          <rect x="1.5" y="1.5" width="13" height="29" rx="1.5" stroke-width="2.5"/>
          <line x1="1.5" y1="26" x2="14.5" y2="26" stroke-width="2"/>
        </svg>
        <span>(555) 014-2937</span>
      </div>
      <div class="contact__web">
        <svg class="icon" width="33" height="33" viewBox="0 0 34 34" aria-hidden="true" stroke-width="2.5">
          <circle cx="17" cy="17" r="15"/>
          <ellipse cx="17" cy="17" rx="6.5" ry="15"/>
          <line x1="2" y1="17" x2="32" y2="17"/>
          <line x1="17" y1="2" x2="17" y2="32"/>
        </svg>
        <span>www.hireavorlatrikebrenmoor.example</span>
      </div>
    </div>
    <div class="tagline">Rentals available hourly or daily. Book online</div>
  </section>

  <section class="card card--blue">
    <div class="hero">
      <div class="hero__vehicle" role="img" aria-label="Line illustration of a three-wheeled roadster"></div>
      <div class="hero__title">Hire</div>
      <div class="hero__subtitle">a Vorlatrike Brenmoor</div>
    </div>
    <div class="contact">
      <div class="contact__phone">
        <svg class="icon" width="16" height="32" viewBox="0 0 16 32" aria-hidden="true">
          <rect x="1.5" y="1.5" width="13" height="29" rx="1.5" stroke-width="2.5"/>
          <line x1="1.5" y1="26" x2="14.5" y2="26" stroke-width="2"/>
        </svg>
        <span>(555) 014-2937</span>
      </div>
      <div class="contact__web">
        <svg class="icon" width="33" height="33" viewBox="0 0 34 34" aria-hidden="true" stroke-width="2.5">
          <circle cx="17" cy="17" r="15"/>
          <ellipse cx="17" cy="17" rx="6.5" ry="15"/>
          <line x1="2" y1="17" x2="32" y2="17"/>
          <line x1="17" y1="2" x2="17" y2="32"/>
        </svg>
        <span>www.hireavorlatrikebrenmoor.example</span>
      </div>
    </div>
    <div class="tagline">Rentals available hourly or daily. Book online</div>
  </section>

</main>
</body>
</html>
```